依頼詳細
このたびは、「緑茶ハイ・緑茶」専用メニュー表(A4片面)のデザインを募集いたします。

【メニュー表に入れていただきたい要素】
・ロゴ「凪色 Harbor」を、おしゃれなレトロ調で作成。メニュー表の上端にロゴを入れる。
・ユーモアで面白さもありつつ、少し高級感もあるデザイン。
・シリーズ化できる(これから緑茶以外にも紅茶ハイなども展開する可能性があります)
・「飲むならこの緑茶ハイがいいな!」と思われるようなデザインやキャッチコピー。
・飲食店の他メニュー表と一緒に置いていて、目を引くデザイン。

【コンペの流れ】
①ご応募ください。
②作成したデザインをご提出ください。
③コンペ終了後、採用者の選定をさせていただきます。

【デザイン提出方法】
PDFデータまたは、AIデータをお送りください。
※採用させていただいた場合、最終納品はイラストレーター形式(.ai)にてお願いします。

【備考】
ご提案いただいたデザインの編集依頼をすることがございます。
納期まで余裕をもってご提案頂けますと幸いです。
納期を過ぎてのご提案は受け付けておりませんので、予めご了承ください。
注意点】
コンペで採用となった場合、著作権は弊社に帰属します。

【継続依頼について】
スキル、センス、クオリティの高さなどにより、継続的な依頼を検討いたします。
記載項目
【メニュー表に入れていただきたい内容】
・緑茶ハイと緑茶の写真画像(デザイナー様の選定でお願いします)
・「緑茶ハイと緑茶」の値段が入れられる場所
(金額は仮で¥500と記載をお願いします)
・とっても美味しい静岡県産掛川市の茶葉を使用。
・無添加、無農薬のお茶粉。
・お茶粉のスティック写真を盛り込む(添付画像データをお使いください)。
※商品チラシデータを添付しています。
栄養や安全性、美味しさの詳細が書かれていますのでご覧ください。
サイズ
A4
ページ数
片面
希望イメージ
シンプル 複雑
単色 カラフル
暗い 明るい
日常 高級
遊び心 厳粛
未来的 伝統的
女性的 男性的
希望する色
緑系
納品ファイル
• イラストレーター形式 (.ai)
〆切を4/5に延長させていただきました!
どうか、デザイナーの方々のお力を貸してください!
よろしくお願いいたします。
みなさまのご協力をお待ちしております。
よろしくお願いいたします!
■ 選んだ理由

弊社のイメージするデザインに1番近かったため。

■ 提案者全員のお礼・コメント

素敵なデザインを作成していただき、ありがとうございます!

```html
<!DOCTYPE html>
<html lang="ja">
<head>
<meta charset="utf-8">
<title>凪色 Harbor 緑茶編 メニュー</title>
<link href="https://fonts.googleapis.com/css2?family=Zen+Old+Mincho:wght@700;900&family=M+PLUS+Rounded+1c:wght@500;800&family=Kaisei+Decol:wght@700&display=swap" rel="stylesheet">
<style>
:root{
  --stripe-a:#8fb84a;
  --stripe-b:#a4c85e;
  --deep-green:#2f5a1c;
  --mid-green:#4f8a2a;
  --price-green:#6aa33a;
  --panel:#fbfdf5;
  --gold:#f2c433;
  --ink:#3a3a2a;
  --accent:#e48a1f;
}
*{margin:0;padding:0;box-sizing:border-box}
html,body{width:846px;height:1200px;overflow:hidden}
body{
  position:relative;
  background:repeating-linear-gradient(90deg,var(--stripe-a) 0 28px,var(--stripe-b) 28px 56px);
  font-family:"M PLUS Rounded 1c",sans-serif;
  color:var(--ink);
}
.masthead{position:absolute;left:0;top:18px;width:846px;text-align:center}
.brand{
  font-family:"Zen Old Mincho",serif;font-weight:900;
  font-size:82px;line-height:1;color:var(--gold);letter-spacing:2px;
  margin-left:-60px;
}
.brand-sub{
  font-family:"Zen Old Mincho",serif;font-weight:700;
  font-size:18px;color:#fff;letter-spacing:6px;margin-top:6px;margin-left:-60px;
}
.brand-sub::before,.brand-sub::after{content:"";display:inline-block;width:50px;height:2px;background:#fff;vertical-align:middle;margin:0 12px}
.badge{position:absolute;right:42px;top:22px;width:90px;height:90px;border-radius:50%;background:var(--deep-green);border:4px solid #fff}
.panel{position:absolute;left:56px;top:170px;width:728px;height:952px;background:var(--panel);border-radius:18px;border:4px solid var(--mid-green)}
.ribbon{
  position:absolute;left:44px;top:-14px;width:640px;height:46px;
  background:var(--deep-green);color:#fff;text-align:center;
  font-family:"Zen Old Mincho",serif;font-weight:700;font-size:24px;line-height:46px;letter-spacing:4px;
}
.photo{position:absolute;border-radius:14px}
.glass-high{left:52px;top:70px;width:236px;height:400px;background:linear-gradient(180deg,#b9d98a,#4f8f22 60%,#3d7417)}
.glass-tea{left:436px;top:70px;width:236px;height:400px;background:linear-gradient(180deg,#c2de93,#5a9a2a 60%,#417a1b)}
.catch{
  position:absolute;left:308px;top:70px;writing-mode:vertical-rl;
  font-family:"Kaisei Decol",serif;font-weight:700;font-size:30px;line-height:44px;color:var(--deep-green);
}
.catch .lead{color:var(--ink)}
.item{position:absolute;text-align:center;width:260px}
.item-high{left:40px;top:494px}
.item-tea{left:424px;top:494px}
.item-name{font-family:"Zen Old Mincho",serif;font-weight:900;font-size:48px;color:var(--deep-green);line-height:1.2}
.price{margin:14px auto 0;width:236px;height:54px;border-radius:10px;background:var(--price-green);color:#fff;font-weight:800;font-size:32px;line-height:54px}
.feature{position:absolute;left:0;top:700px;width:728px;height:220px}
.attention{position:absolute;left:-10px;top:0;width:58px;height:58px;border-radius:50%;background:var(--accent);color:#fff;font-weight:800;font-size:18px;line-height:58px;text-align:center}
.attention-note{position:absolute;left:56px;top:8px;font-size:13px;color:var(--ink)}
.powder{left:50px;top:50px;width:150px;height:90px;border-radius:50%;background:radial-gradient(circle,#7fae3a,#4d8220)}
.stick{left:218px;top:0;width:30px;height:150px;border-radius:4px;background:linear-gradient(180deg,#e7a14a,#d04c7d,#6a3d9a);transform:rotate(12deg)}
.claims{position:absolute;left:274px;top:56px;font-weight:800;font-size:26px;color:var(--mid-green);line-height:50px}
.claims li{list-style:none;border-bottom:2px solid var(--price-green)}
.disclaimer{position:absolute;right:40px;top:1140px;font-size:12px;color:#fff}
</style>
</head>
<body>
<header class="masthead">
  <div class="brand">凪色 Harbor</div>
  <div class="brand-sub">なぎいろ</div>
</header>
<div class="badge" aria-hidden="true"></div>

<main class="panel">
  <div class="ribbon">緑茶編</div>
  <div class="photo glass-high" role="img" aria-label="氷の入ったグラスの緑茶ハイ"></div>
  <div class="photo glass-tea" role="img" aria-label="ストローを挿したグラスの緑茶"></div>
  <p class="catch"><span class="lead">とっても美味しい</span><br>静岡県産掛川市の茶葉</p>

  <section class="item item-high">
    <h2 class="item-name">緑茶ハイ</h2>
    <p class="price">¥500</p>
  </section>
  <section class="item item-tea">
    <h2 class="item-name">緑茶</h2>
    <p class="price">¥500</p>
  </section>

  <section class="feature">
    <div class="attention">注目</div>
    <p class="attention-note">お茶粉 栄養素配合♪</p>
    <div class="photo powder" role="img" aria-label="茶葉とお茶粉"></div>
    <div class="photo stick" role="img" aria-label="お茶粉のスティック包装"></div>
    <ul class="claims">
      <li>無添加、無農薬のお茶粉</li>
      <li>栄養素青汁の約5倍</li>
    </ul>
  </section>
</main>
<p class="disclaimer">※画像はイメージです。</p>
</body>
</html>
```